Gym flyer for personal training

I am looking for a one page poster to put up in the gym where I train clients. I might also use this in other public places. My business is called Doug Kellerman Fit and the logo design and business cards were done through QT/ Lumo Press. My services to be marketed are: One on One Personal Training and Small Group Training. I would also like to feature a photo of me so that clients can recognize me on the floor. My training style is not hard core of Torqwell like so I would not want any stock photos featuring this type of training. I will upload a photo. Please include "PTQB Certified Personal Trainer". I would also like to have the text: "New Trainer at Harbor Fitness!"

Target Market(s)

current gym goers

Industry/Entity Type

Business

Colors
3276b5
52b3dd
33a6d7
33b8a4
faa54b
f68e4e
f37122
f78f20

Requirements
Must have
• Name, e mail, phone number. my logo
Should not have
• no stock pictures of big guys lifting heavy weight in a dirty gym

```html
<!DOCTYPE html>
<html lang="en">
<head>
<meta charset="utf-8">
<title>Doug Kellerman Fit – New Trainer Poster</title>
<link href="https://fonts.googleapis.com/css2?family=Oswald:wght@400;500;600;700&family=Roboto+Condensed:wght@400;700&display=swap" rel="stylesheet">
<style>
  :root {
    --ink: #2b2c2e;
    --ink-deep: #1f2022;
    --steel: #4a4c50;
    --white: #ffffff;
    --sky: #33a6d7;
    --sky-light: #52b3dd;
    --orange: #f78f20;
    --green: #8cc63f;
    --muted: #c9cacc;
  }
  * { box-sizing: border-box; margin: 0; padding: 0; }
  html, body { width: 739px; height: 1200px; overflow: hidden; background: #e9e7e3; }
  .poster {
    position: relative; width: 739px; height: 1200px; overflow: hidden;
    background: var(--ink);
    font-family: "Oswald", "Roboto Condensed", sans-serif;
    color: var(--white);
  }
  .gym-backdrop {
    position: absolute; left: 0; top: 190px; width: 739px; height: 520px;
    background: radial-gradient(ellipse at 60% 40%, #5a5c60 0%, #3a3b3e 45%, var(--ink) 80%);
    opacity: .9;
  }
  .brand {
    position: absolute; top: 118px; left: 0; width: 100%;
    text-align: center; font-weight: 700; font-size: 50px; letter-spacing: 1px;
    color: var(--sky); text-transform: uppercase;
  }
  .headline { position: absolute; left: 70px; top: 228px; width: 600px; }
  .headline .big {
    display: block; font-weight: 600; font-size: 132px; line-height: 1; letter-spacing: 1px;
    text-transform: uppercase;
  }
  .headline .gym {
    display: block; text-align: right; font-weight: 500; font-size: 36px;
    text-transform: uppercase; margin-top: 2px;
  }
  .services {
    position: absolute; left: 70px; top: 520px; width: 600px;
    font-family: "Roboto Condensed", sans-serif; font-weight: 700;
    color: var(--orange); text-transform: uppercase; font-size: 30px; line-height: 1.2;
  }
  .services .amp { font-size: 18px; text-transform: none; margin: 0 6px 0 8px; }
  .services .second { padding-left: 185px; display: block; }
  .trainer-band {
    position: absolute; left: 0; top: 626px; width: 739px; height: 196px;
    background: var(--sky);
  }
  .with-tag {
    position: absolute; left: 56px; top: 70px; width: 36px; height: 110px;
    background: var(--white); color: var(--sky);
    display: flex; align-items: center; justify-content: center;
  }
  .with-tag span {
    transform: rotate(-90deg); font-weight: 700; font-size: 22px; letter-spacing: 2px;
  }
  .trainer-name {
    position: absolute; left: 108px; top: 10px;
    font-weight: 700; font-size: 84px; line-height: .98; text-transform: uppercase;
  }
  .trainer-photo {
    position: absolute; right: 48px; top: 12px; width: 172px; height: 172px;
    border: 4px solid var(--white);
    background: linear-gradient(160deg, #9fcbe4 0%, #c79a7d 55%, #4f6a86 100%);
  }
  .credential {
    position: absolute; left: 70px; top: 836px;
    font-family: "Roboto Condensed", sans-serif; font-weight: 700;
    font-size: 20px; text-transform: uppercase;
  }
  .footer {
    position: absolute; left: 0; top: 900px; width: 739px; height: 300px;
    background: var(--ink-deep);
  }
  .footer-rule { position: absolute; left: 60px; top: 60px; width: 150px; height: 5px; background: var(--green); }
  .footer-brand {
    position: absolute; left: 60px; top: 118px;
    font-weight: 700; font-size: 22px; color: var(--sky); text-transform: uppercase;
  }
  .contact { position: absolute; right: 60px; top: 44px; text-align: right; }
  .contact .call {
    font-family: "Roboto Condensed", sans-serif; font-weight: 700;
    font-size: 24px; text-transform: uppercase; letter-spacing: .5px;
  }
  .contact .phone {
    display: flex; align-items: center; justify-content: flex-end; gap: 10px;
    font-weight: 600; font-size: 52px; color: var(--green); line-height: 1.15;
  }
  .contact .email { font-family: "Roboto Condensed", sans-serif; font-size: 20px; color: var(--muted); }
</style>
</head>
<body>
<main class="poster">
  <div class="gym-backdrop" role="img" aria-label="Dimmed close-up of gym dumbbells on a rack"></div>

  <div class="brand">Doug Kellerman Fit</div>

  <h1 class="headline">
    <span class="big">New</span>
    <span class="big">Trainer</span>
    <span class="gym">At Harbor Fitness!</span>
  </h1>

  <p class="services">
    Personal Training<br>
    <span class="second"><span class="amp">and</span>Small Group Training</span>
  </p>

  <section class="trainer-band">
    <div class="with-tag"><span>WITH</span></div>
    <h2 class="trainer-name">Doug<br>Kellerman</h2>
    <div class="trainer-photo" role="img" aria-label="Portrait photo of trainer Doug Kellerman"></div>
  </section>

  <p class="credential">• PTQB Certified Personal Trainer</p>

  <footer class="footer">
    <div class="footer-rule"></div>
    <div class="footer-brand">Doug Kellerman Fit</div>
    <div class="contact">
      <p class="call">Contact Doug Kellerman Today</p>
      <p class="phone">
        <svg width="30" height="30" viewBox="0 0 24 24" aria-hidden="true"><path fill="#8cc63f" d="M6.6 10.8a15.1 15.1 0 0 0 6.6 6.6l2.2-2.2a1 1 0 0 1 1-.25 11.4 11.4 0 0 0 3.6.57 1 1 0 0 1 1 1V20a1 1 0 0 1-1 1A17 17 0 0 1 3 4a1 1 0 0 1 1-1h3.5a1 1 0 0 1 1 1c0 1.25.2 2.45.57 3.57a1 1 0 0 1-.25 1z"/></svg>
        (555) 014-2280
      </p>
      <p class="email">doug@kellermanfit.com</p>
    </div>
  </footer>
</main>
</body>
</html>
```